Owen Tasker Studios Business Card

Looking for a clear, modern, elegant, sharp business card that conveys a professional yet edgy image to my business as a wedding, portrait, and travel photographer. Would like something that looks vintage yet modern. Need a new business card to grow my business. We are growing the business for Wedding and Event Photography as well as fine art Photography. (Mostly Landscapes)
Updates

I’m looking through designs now but I have a new logo that i want using please.

New logo uploaded please redesign using that

PLEASE ALL DESIGNERS LOOK IN BRIEF FOR NEW LOGO

Target Market(s)

Brides, Grooms, Families with Kids, People looking for Fine Art Photography Artwork

Industry/Entity Type

Photographer

Contact Information for Business Card

Unsure

Font styles to use
Serif

Colors

Designer to choose colors to be used in the design.

Requirements
Must have
• My Website:
• http://taskerlens.examplefolio.net
• Phone:
• 323-481-5206
• Email:
• owentaskerlens@mailbox-example.net
Nice to have
• Would like a sort of shine on the printing finish.
• I like black I think it looks good on a business card.
• Can try working with my logo (png that I've attached)

```html
<!DOCTYPE html>
<html lang="en">
<head>
<meta charset="utf-8">
<title>Owen Tasker Studios Business Card</title>
<link rel="stylesheet" href="https://fonts.googleapis.com/css2?family=Josefin+Sans:wght@300&family=Noto+Serif:wght@400;700&display=swap">
<style>
  :root {
    --backdrop: #3a3b3e;
    --card-dark: #0c0f18;
    --card-light: #ffffff;
    --ink-light: #f2f2f2;
    --ink-dark: #1b1b1b;
    --rule: #2a2a2a;
  }
  html, body {
    margin: 0;
    width: 1200px;
    height: 880px;
    overflow: hidden;
    background: var(--backdrop);
  }
  .canvas {
    position: relative;
    width: 1200px;
    height: 880px;
  }
  .card {
    position: absolute;
    width: 600px;
    height: 343px;
    border-radius: 22px;
    box-shadow: 0 10px 30px rgba(0,0,0,0.35);
  }
  .card-front {
    left: 90px;
    top: 80px;
    background: var(--card-dark);
    display: flex;
    align-items: center;
    justify-content: center;
  }
  .brand {
    display: flex;
    align-items: center;
    gap: 16px;
    color: var(--ink-light);
    font-family: "Josefin Sans", sans-serif;
    font-weight: 300;
    font-size: 30px;
    letter-spacing: 2px;
    text-transform: uppercase;
  }
  .brand-square {
    width: 40px;
    height: 40px;
    border: 1.5px solid var(--ink-light);
    box-sizing: border-box;
  }
  .card-back {
    left: 510px;
    top: 460px;
    background: var(--card-light);
    display: flex;
    align-items: center;
    padding-left: 95px;
    box-sizing: border-box;
    color: var(--ink-dark);
    font-family: "Noto Serif", serif;
  }
  .identity {
    text-align: right;
    padding-right: 16px;
  }
  .identity-name {
    font-size: 19px;
    letter-spacing: 0.5px;
    text-transform: uppercase;
    line-height: 1.1;
  }
  .identity-role {
    font-size: 14px;
    line-height: 1.2;
  }
  .divider {
    width: 1px;
    height: 70px;
    background: var(--rule);
  }
  .contact {
    list-style: none;
    margin: 0;
    padding: 0 0 0 16px;
    font-size: 12.5px;
    line-height: 1.65;
  }
  .contact-label {
    font-weight: 700;
  }
</style>
</head>
<body>
<main class="canvas">
  <section class="card card-front">
    <div class="brand">
      <span class="brand-square"></span>
      <span class="brand-name">Owen Tasker Studios</span>
    </div>
  </section>

  <section class="card card-back">
    <div class="identity">
      <div class="identity-name">Owen Tasker</div>
      <div class="identity-role">Photographer</div>
    </div>
    <div class="divider"></div>
    <ul class="contact">
      <li><span class="contact-label">Phone:</span> 323-481-5206</li>
      <li><span class="contact-label">Email:</span> owentaskerlens@mailbox-example.net</li>
      <li><span class="contact-label">Web:</span> http://taskerlens.examplefolio.net</li>
    </ul>
  </section>
</main>
</body>
</html>
```